Winter is coming, is your home ready ?

We are a full service Insulation contracting services company . We insulate new and existing homes, commercial and industrial buildings.

We are looking for a billboard that shows our harsh winter approaching and a call to action for getting a free estimate.

We specialize in spray foam insulation but it doesn't need to be called out on the billboard if too much text make it looks too busy.

We do enjoy humor if its something that could work and keep people thinking of us.
Company web site is www.brivanthermal.com
Company phone number is 847-392-5816

```html
<!DOCTYPE html>
<html lang="en">
<head>
<meta charset="utf-8">
<title>Brivan Thermal – Winter Billboard</title>
<link href="https://fonts.googleapis.com/css2?family=Montserrat:wght@800&family=Oswald:wght@400;500;600&display=swap" rel="stylesheet">
<style>
  :root {
    --green: #b2c034;
    --ink: #161616;
    --charcoal: #454545;
    --bar: #565656;
    --paper: #ffffff;
    --stage: #e6e6e6;
  }
  html, body {
    margin: 0;
    width: 923px;
    height: 1200px;
    overflow: hidden;
    background: var(--stage);
  }
  .billboard {
    position: absolute;
    left: 30px;
    top: 385px;
    width: 863px;
    height: 430px;
    background: linear-gradient(120deg, #f6f6f6 0%, #ffffff 45%, #f4f4f4 100%);
    box-shadow: 0 6px 18px rgba(0,0,0,.35);
    overflow: hidden;
  }
  .shapes { position: absolute; inset: 0; }
  .headline {
    position: absolute;
    left: 40px;
    margin: 0;
    font-family: 'Montserrat', sans-serif;
    font-weight: 800;
    line-height: 1;
    white-space: nowrap;
  }
  .headline.dark { color: var(--ink); font-size: 51px; }
  .headline.accent { color: var(--green); font-size: 67px; }
  .line-1 { top: 30px; }
  .line-2 { top: 80px; }
  .line-3 { top: 145px; }
  .line-4 { top: 194px; }
  .house-art {
    position: absolute;
    left: 478px;
    top: 30px;
    width: 352px;
    height: 205px;
    border-radius: 6px;
    background: linear-gradient(180deg, #d9e27a 0%, #f0c650 30%, #e9e9e9 55%, #d4d4d4 100%);
    opacity: .85;
  }
  .callout {
    position: absolute;
    left: 360px;
    top: 222px;
    width: 200px;
    margin: 0;
    text-align: center;
    font-family: 'Oswald', sans-serif;
    font-weight: 400;
    font-size: 15.5px;
    line-height: 18.5px;
    color: var(--paper);
    text-transform: uppercase;
  }
  .callout em { font-style: normal; font-weight: 500; color: var(--green); }
  .tagline {
    position: absolute;
    left: 38px;
    top: 290px;
    margin: 0;
    font-family: 'Oswald', sans-serif;
    font-weight: 500;
    font-size: 25px;
    line-height: 31px;
    color: var(--paper);
    text-transform: uppercase;
    white-space: nowrap;
  }
  .brand-box {
    position: absolute;
    left: 570px;
    top: 273px;
    width: 261px;
    height: 85px;
    background: var(--paper);
    border: 1.5px solid var(--green);
    border-bottom: none;
    border-radius: 10px 10px 0 0;
    display: flex;
    align-items: center;
    justify-content: center;
    box-sizing: border-box;
  }
  .brand-name {
    font-family: 'Oswald', sans-serif;
    font-weight: 500;
    font-size: 30px;
    color: var(--bar);
    letter-spacing: .5px;
  }
  .cta-bar {
    position: absolute;
    left: 0;
    top: 358px;
    width: 863px;
    height: 72px;
    background: var(--bar);
    display: flex;
    align-items: center;
    font-family: 'Oswald', sans-serif;
    font-weight: 600;
    white-space: nowrap;
  }
  .cta-label { margin-left: 38px; font-size: 37px; color: var(--paper); }
  .phone-icon { margin: 0 6px 0 8px; }
  .cta-phone { font-size: 37px; color: var(--green); }
  .divider {
    width: 1.5px;
    height: 30px;
    background: var(--paper);
    margin: 0 16px 0 20px;
  }
  .cta-web { font-size: 29px; color: var(--green); }
  .cta-web span { color: var(--paper); }
</style>
</head>
<body>
  <div class="billboard">
    <svg class="shapes" width="863" height="430" viewBox="0 0 863 430">
      <polygon class="band" fill="#b2c034" points="0,280 327,280 350,312 863,312 863,358 0,358"/>
      <polygon class="wedge-top" fill="#b2c034" points="444,216 516,193 516,216"/>
      <polygon class="wedge-left" fill="#b2c034" points="333,236 356,220 364,264"/>
      <polygon class="callout-panel" fill="#454545" points="352,216 566,203 555,325 365,291"/>
    </svg>

    <p class="headline dark line-1">WINTER IS</p>
    <p class="headline accent line-2">COMING</p>
    <p class="headline dark line-3">IS YOUR HOME</p>
    <p class="headline accent line-4">READY?</p>

    <div class="house-art" role="img" aria-label="3D illustration of a white house with a rainbow energy-rated roof beside a sign showing an A to G energy efficiency label"></div>

    <p class="callout">We insulate<br><em>new and existing homes,</em><br><em>commercial</em> and<br><em>industrial</em> buildings.</p>

    <p class="tagline">We are a full service<br>insulation contracting services company.</p>

    <div class="brand-box"><span class="brand-name">Brivan Thermal, Inc.</span></div>

    <div class="cta-bar">
      <span class="cta-label">FREE ESTIMATE</span>
      <svg class="phone-icon" width="28" height="28" viewBox="0 0 28 28" aria-hidden="true">
        <circle cx="14" cy="14" r="12.5" fill="none" stroke="#b2c034" stroke-width="2"/>
        <circle cx="14" cy="14" r="9.5" fill="#b2c034"/>
        <path d="M10.2 8.6c.5-.4 1.1-.3 1.4.2l1.2 1.9c.3.5.2 1-.2 1.3l-.8.6c.6 1.4 1.6 2.5 3 3.2l.6-.8c.4-.4.9-.5 1.3-.2l1.9 1.2c.5.3.6.9.2 1.4l-.7.9c-.6.7-1.6.9-2.5.5-3-1.3-5.2-3.6-6.4-6.6-.3-.9-.1-1.9.6-2.5z" fill="#ffffff"/>
      </svg>
      <span class="cta-phone">847-392-5816</span>
      <span class="divider"></span>
      <span class="cta-web">BrivanThermal<span>.com</span></span>
    </div>
  </div>
</body>
</html>
```